International Property Consultancy

Brief Overview:

I need a dynamic and well designed website that is easy to use and understand. It has to be unique and different to generic templates that most websites seem to be these days. PLEASE NO GENERIC TEMPLATES FROM THE INTERNET.

Our business has 10 years experience working on struggling international developments that we then work in-house for to turn around and brings bout success. We stay within a project often for long periods of time until success is achieved. We are unique in our approach and completely different to the standard routes to market for many developments. The site is for developers to see what we have done in regards to previous projects, as such we want to incorporate video into this site with a strong design aesthetic. There will be videos of the past projects we have worked on, which will act as case studies.

I like very simple but punchy websites, that people can navigate and understand very easily. Also a big fan of unique and well thought out design aesthetic.

Initial Site layout thoughts:

1) Homepage:
2) About Us
3) What we've done / Work
This part has the projects we have worked on (France, Portugal, London, Morocco). Each one will have some video content and photo images, but also would be good to have a succinct way to mention what we did and the successes in a clever and punchy way.

4) Contact Us

* This is just a guideline. Would be open to input and creative direction on your own part.

*More details and websites we like can be seen in the brief doc attached.

PLEASE VIEW THE WIREFRAME WORD DOC ATTACHED.

Here there are also some more examples to help:

Here are just a few examples of websites and what I like about them:

- www.velmoro.com (clean, nice geometric design aesthetic, good animation when loading and changing pages well thought out all though also coulee be considered a bit dull and basic after the initial homepage slide)
- https://www.farbridgehub.net (Clean site, quite clinical, lacks video content and doesn't engage greatly).
- https://ruskotile.com (minimal, and like how it mixes the design aesthetic more with video and photo content)

- https://www.amberquillworks.com (like the layout of this and how it displays the projects and work section)

- https://brisk.com (Good use of video content)

- https://loomfield.studio (minimal to the point and mixes design with video and animation etc...)

Here is another couple of cool websites that may help give you some direction: https://halvenquay.com www.brisk.com

Hi there, One of the things I thought would be good on the homepage is to add the logo with a 'digital landscape' before flicking down into a slide with video content of the projects... Just an idea but have posted some pics in the brief. We would get this animated for the site. But if you have better ideas, please do run with them. Thanks,

Target Market(s)

Property developers

Number of Pages Required

4 page

Font styles to use
Other font styles liked:
• Read brief

Requirements
Must have
• Needs to be clean, dynamic and easy to follow on desktop and mobile. We will use it as a kind of portfolio website so will need to embed video of past projects we have worked on.

Read brief in docs.
Nice to have
• Clean
Should not have
• Not be another generic template website.
Not have random property stock photos. (We are not a property agency).

```html
<!DOCTYPE html>
<html lang="en">
<head>
<meta charset="utf-8">
<title>Ostrova — International Property Consultancy</title>
<link rel="stylesheet" href="https://fonts.googleapis.com/css2?family=Outfit:wght@300;400;600;700;800&display=swap">
<style>
  :root {
    --ink-navy: #262b57;
    --teal-deep: #15465a;
    --teal-head: #174a5e;
    --teal-mid: #1d5a6e;
    --grey-text: #4b4f66;
    --line-light: #e6e8ec;
    --white: #ffffff;
  }
  * { margin: 0; padding: 0; box-sizing: border-box; }
  html, body { width: 668px; height: 1200px; overflow: hidden; background: var(--white); }
  body { position: relative; font-family: "Outfit", sans-serif; color: var(--ink-navy); }

  .site-header { position: absolute; top: 0; left: 0; width: 668px; height: 49px; border-bottom: 1px solid var(--line-light); }
  .brand { position: absolute; font-weight: 600; letter-spacing: -0.5px; }
  .site-header .brand { left: 59px; top: 12px; font-size: 22px; color: var(--ink-navy); }
  .main-nav a { position: absolute; top: 20px; font-size: 7.5px; color: var(--grey-text); text-decoration: none; letter-spacing: 0.2px; }
  .main-nav a.is-active { font-weight: 700; color: var(--ink-navy); }

  .hero-art { position: absolute; left: 44px; top: 121px; width: 305px; height: 205px; border-radius: 50%;
    background: radial-gradient(ellipse at center, #e3ebef 0%, #eef3f5 55%, #ffffff 75%); }
  .hero-title { position: absolute; left: 387px; top: 146px; font-size: 43px; line-height: 41px; font-weight: 700; color: var(--teal-head); letter-spacing: -0.5px; }
  .hero-lede { position: absolute; left: 388px; top: 246px; font-size: 21px; line-height: 25px; font-weight: 300; color: var(--teal-head); }
  .scroll-cue { position: absolute; left: 300px; top: 380px; width: 68px; text-align: center; font-size: 7.5px; color: var(--grey-text); }
  .scroll-cue svg { display: block; margin: 3px auto 0; }

  .showreel { position: absolute; left: 0; top: 433px; width: 668px; height: 389px;
    background: linear-gradient(135deg, #1a4a5e 0%, #2e5d70 45%, #234f63 70%, #15465a 100%); }
  .showreel .brand { left: 62px; top: 86px; font-size: 24px; font-weight: 400; color: var(--white); }
  .showreel .brand-dot { display: inline-block; width: 30px; height: 30px; border-radius: 50%; background: var(--white); vertical-align: middle; margin-right: 12px; }
  .showreel-title { position: absolute; left: 59px; top: 147px; font-size: 22px; line-height: 30px; font-weight: 700; color: var(--white); }
  .stat-number { position: absolute; left: 62px; top: 222px; font-size: 20px; font-weight: 700; color: var(--white); }
  .stat-label { position: absolute; left: 62px; top: 246px; font-size: 14px; font-weight: 600; color: var(--white); }
  .play-button { position: absolute; left: 436px; top: 148px; }
  .slide-rail { position: absolute; left: 635px; top: 136px; }

  .approach { position: absolute; left: 0; top: 822px; width: 668px; height: 284px;
    background: linear-gradient(180deg, #ffffff 0%, #f7f6f3 55%, #efede8 100%); }
  .approach-text { position: absolute; left: 100px; top: 87px; width: 468px; text-align: center; font-size: 16px; line-height: 20.5px; font-weight: 700; color: var(--ink-navy); }
  .cta-button { position: absolute; left: 282px; top: 166px; width: 104px; height: 25px; border-radius: 13px; background: var(--teal-deep); color: var(--white); font-size: 8px; font-weight: 600; text-align: center; line-height: 25px; text-decoration: none; }

  .site-footer { position: absolute; left: 0; top: 1106px; width: 668px; height: 94px; background: var(--teal-deep); color: var(--white); }
  .site-footer .brand { left: 62px; top: 16px; font-size: 20px; color: var(--white); }
  .footer-nav a { position: absolute; top: 24px; font-size: 7.5px; font-weight: 700; color: var(--white); text-decoration: none; }
  .social-dot { position: absolute; top: 20px; width: 16px; height: 16px; border-radius: 50%; background: var(--white); }
  .footer-rule { position: absolute; left: 0; top: 60px; width: 655px; height: 1px; background: rgba(255,255,255,0.18); }
  .copyright { position: absolute; left: 63px; top: 72px; font-size: 7px; font-weight: 300; }
  .legal { position: absolute; left: 507px; top: 71px; font-size: 6.5px; font-weight: 300; }
</style>
</head>
<body>
  <header class="site-header">
    <div class="brand">ostrova.</div>
    <nav class="main-nav">
      <a class="is-active" href="#" style="left:311px">HOME</a>
      <a href="#" style="left:368px">ABOUT US</a>
      <a href="#" style="left:442px">WHAT WE'VE DONE</a>
      <a href="#" style="left:546px">CONTACT US</a>
    </nav>
  </header>

  <section class="hero">
    <div class="hero-art" role="img" aria-label="Line illustration of consulting icons: charts, gears, globe on a screen and a team"></div>
    <h1 class="hero-title">We are<br>Ostrova</h1>
    <p class="hero-lede">We fulfill international<br>property developments</p>
    <div class="scroll-cue">Scroll
      <svg width="9" height="15" viewBox="0 0 9 15"><rect x="0.6" y="0.6" width="7.8" height="13.8" rx="3.9" fill="none" stroke="#262b57" stroke-width="0.9"/><line x1="4.5" y1="3" x2="4.5" y2="6" stroke="#262b57" stroke-width="0.9"/></svg>
    </div>
  </section>

  <section class="showreel" role="img" aria-label="Video still of a team meeting around a table, tinted teal">
    <div class="brand"><span class="brand-dot"></span>Quellen</div>
    <h2 class="showreel-title">AUGIAT IN PEDE FUSCE<br>TELLUS SED METUS</h2>
    <div class="stat-number">50 Project</div>
    <div class="stat-label">we delivered</div>
    <svg class="play-button" width="62" height="62" viewBox="0 0 62 62"><circle cx="31" cy="31" r="28" fill="none" stroke="#fff" stroke-width="4"/><path d="M25 20 L40 31 L25 42 Z" fill="#fff"/></svg>
    <svg class="slide-rail" width="3" height="98" viewBox="0 0 3 98">
      <rect x="0.5" y="0" width="1.6" height="20" fill="#fff"/>
      <rect x="0.8" y="26" width="0.8" height="20" fill="rgba(255,255,255,0.6)"/>
      <rect x="0.8" y="52" width="0.8" height="20" fill="rgba(255,255,255,0.6)"/>
      <rect x="0.8" y="78" width="0.8" height="20" fill="rgba(255,255,255,0.6)"/>
    </svg>
  </section>

  <section class="approach" role="img" aria-label="Faint wireframe drawing of a city skyline">
    <p class="approach-text">We deliver a unique and truly bespoke approach to delivering international developments to market, with over 10 years success around the world.</p>
    <a class="cta-button" href="#">See our Work &rarr;</a>
  </section>

  <footer class="site-footer">
    <div class="brand">ostrova.</div>
    <nav class="footer-nav">
      <a href="#" style="left:211px">ABOUT US</a>
      <a href="#" style="left:276px">WHAT WE'VE DONE</a>
      <a href="#" style="left:374px">CONTACT US</a>
    </nav>
    <span class="social-dot" style="left:532px" aria-label="Social link"></span>
    <span class="social-dot" style="left:556px" aria-label="Social link"></span>
    <span class="social-dot" style="left:579px" aria-label="Social link"></span>
    <div class="footer-rule"></div>
    <div class="copyright">© 2020 ostrova. All Right Reserved</div>
    <div class="legal">Privacy Policy &nbsp;&nbsp;|&nbsp;&nbsp; Terms of Use</div>
  </footer>
</body>
</html>
```